KT MACHINERY DEPOT

we sell used heavy equipment look at our current website www.halvikfreight.com we are looking for a easier site to use with our new name

```html
<!DOCTYPE html>
<html lang="en">
<head>
<meta charset="utf-8">
<title>KT Machinery Depot — Used Heavy Equipment</title>
<link rel="stylesheet" href="https://fonts.googleapis.com/css2?family=Outfit:wght@400;500;600&display=swap">
<style>
:root{
  --navy:#233e85;
  --gold:#a8844c;
  --cream:#fdfbef;
  --sand:#ebe1cb;
  --ink:#1c1c1c;
  --muted:#4a4a4a;
  --white:#ffffff;
}
*{box-sizing:border-box;margin:0;padding:0}
html,body{width:1200px;height:4696px;overflow:hidden}
body{position:relative;background:var(--cream);font-family:"Outfit",sans-serif;color:var(--ink)}
.abs{position:absolute}
.hero-wash{left:0;top:0;width:1200px;height:640px;background:
  radial-gradient(ellipse 520px 420px at 0 0,rgba(198,170,120,.55),transparent 70%),
  radial-gradient(ellipse 420px 460px at 1200px 120px,rgba(150,165,190,.65),transparent 70%)}
.topbar{left:0;top:0;width:1200px;height:78px}
.topbar-contact{top:18px;display:flex;align-items:center;gap:12px;color:var(--white);font-size:18px}
.icon-circle{width:40px;height:40px;border-radius:50%;background:var(--white);display:flex;align-items:center;justify-content:center}
.brand{left:128px;top:112px;color:var(--navy);font-weight:600;font-size:22px;display:flex;align-items:center;gap:10px}
.brand-mark{width:22px;height:22px;background:var(--gold);border-radius:50%}
.nav{top:116px;left:418px;display:flex;gap:36px;font-size:15px;font-weight:500}
.btn{display:flex;align-items:center;justify-content:center;font-weight:500;text-decoration:none}
.btn-gold{background:var(--gold);color:var(--white)}
.btn-navy{background:var(--navy);color:var(--white)}
.nav-apply{left:912px;top:104px;width:155px;height:42px;font-size:15px}
.badge{left:174px;top:250px;width:134px;height:134px;border-radius:50%;border:4px solid #9a4a22;background:var(--white)}
.hero-title{left:300px;top:244px;width:600px;text-align:center;font-size:43px;font-weight:500;line-height:50px}
.hero-text{left:262px;top:412px;width:676px;text-align:center;font-size:15.5px;line-height:24px}
.hero-btn{top:534px;height:42px;width:157px;font-size:15px}
.video{left:77px;top:638px;width:1043px;height:628px;border-radius:56px;background:linear-gradient(180deg,#7aa3d8 0%,#b8c3c4 45%,#c9a24a 60%,#8f8f8a 100%);box-shadow:0 6px 14px rgba(0,0,0,.2)}
.play{left:536px;top:912px;width:110px;height:110px;border-radius:50%;background:rgba(168,132,76,.9);display:flex;align-items:center;justify-content:center}
.benefits{left:0;top:1379px;width:1200px;height:511px;background:var(--gold)}
.benefits-title{left:128px;top:1425px;width:600px;color:var(--white);font-size:27px;font-weight:500;line-height:34px}
.benefits-text{left:128px;top:1508px;width:560px;color:var(--white);font-size:14px;line-height:24px}
.feature{color:var(--white);display:flex;gap:20px}
.feature-icon{flex:none;width:44px;height:44px;border-radius:50%;background:var(--white)}
.feature div{width:210px}
.feature h3{font-size:13px;font-weight:600;letter-spacing:1.5px;line-height:16px;margin-bottom:8px}
.feature p{font-size:12.5px;line-height:21px}
.finder{left:781px;top:1342px;width:335px;height:427px;background:var(--white);border-radius:22px;box-shadow:0 4px 16px rgba(0,0,0,.15)}
.finder h2{position:absolute;left:31px;top:44px;color:var(--navy);font-size:22px;font-weight:500}
.field{position:absolute;height:40px;border:2px solid #d9d1bf;display:flex;align-items:center;padding-left:12px;gap:10px;font-size:13px;color:#a8a8a8}
.field-ico{width:22px;height:22px;border:1.5px solid #c9c9c9;border-radius:4px}
.search-btn{position:absolute;left:31px;top:345px;width:275px;height:37px;font-size:16px;gap:8px}
.section-title{left:0;width:1200px;text-align:center;font-size:27px;font-weight:500;line-height:33px}
.section-sub{left:0;width:1200px;text-align:center;font-size:13px;line-height:22px}
.card{width:283px;height:423px;border-radius:0 0 36px 0;overflow:hidden;color:var(--white);text-align:center}
.card.navy{background:var(--navy)}
.card.gold{background:var(--gold)}
.card-photo{height:221px}
.card h3{font-size:20px;font-weight:500;line-height:26px;margin-top:12px}
.card .price{font-size:31px;font-weight:500;margin-top:6px}
.card .details{margin:22px auto 0;width:138px;height:36px;border-radius:18px;background:var(--white);font-size:14px}
.navy .details{color:var(--navy)}
.gold .details{color:var(--gold)}
.sold{position:absolute;right:0;top:0;background:var(--gold);color:var(--white);font-size:20px;padding:4px 18px;border-radius:0 0 0 18px}
.view-all{left:527px;top:3083px;width:157px;height:45px;font-size:17px}
.quote{width:292px;height:157px;background:var(--sand);border-radius:36px 0 0 0;padding:56px 18px 0;font-size:12.5px;line-height:20px}
.person{width:292px;text-align:center;font-size:12.5px;line-height:24px}
.avatar{width:54px;height:54px;border-radius:50%;background:linear-gradient(#c9cdd3,#6b7380);border:3px solid var(--white);margin:0 auto 4px}
.cta{left:133px;top:3843px;width:967px;height:283px;border-radius:40px 0 40px 0;background:linear-gradient(135deg,#3a3731,#6b5a3e 45%,#2a2622);transform:skewX(-4deg)}
.cta-title{left:0;top:3910px;width:1270px;text-align:center;color:var(--white);font-size:28px;font-weight:500}
.cta-text{left:0;top:3955px;width:1270px;text-align:center;color:var(--white);font-size:14px;line-height:24px}
.cta-btn{top:4033px;width:157px;height:42px;font-size:15px}
.btn-outline{border:2px solid var(--white);color:var(--white)}
.vline{width:2px;height:264px;top:4305px;background:var(--gold)}
.quick{left:150px;top:4376px;width:164px;text-align:right}
.quick h4{color:var(--navy);font-size:15px;font-weight:500;margin-bottom:6px}
.quick a{display:block;color:var(--gold);font-size:12px;line-height:25px;text-decoration:none}
.footer-brand{left:380px;top:4410px;width:348px;text-align:center;color:var(--navy);font-size:30px;font-weight:600;line-height:36px}
.footer-brand small{display:block;font-size:13px;font-weight:500;color:var(--gold);line-height:22px}
.socials{left:498px;top:4538px;display:flex;gap:16px}
.socials span{width:18px;height:18px;border-radius:50%;background:var(--navy)}
.contact{left:793px;top:4367px;width:240px}
.contact h4{color:var(--gold);font-size:15px;font-weight:500;margin-bottom:10px}
.contact p{display:flex;gap:10px;color:var(--navy);font-size:12px;line-height:18px;margin-bottom:8px}
.rule{left:106px;top:4606px;width:988px;height:1px;background:#888}
.legal{left:0;top:4637px;width:1200px;display:flex;justify-content:center;gap:18px;font-size:11px}
.legal a{color:var(--navy);text-decoration:underline}
</style>
</head>
<body>
<div class="abs hero-wash"></div>

<svg class="abs topbar" viewBox="0 0 1200 78" aria-hidden="true">
  <path d="M483 0 H1200 V78 H560 C520 78 510 0 483 0 Z" fill="#233e85"/>
</svg>
<div class="abs topbar-contact" style="left:518px">
  <span class="icon-circle"><svg width="20" height="20" viewBox="0 0 24 24"><path d="M6.6 10.8a15 15 0 006.6 6.6l2.2-2.2c.3-.3.7-.4 1-.2 1.1.4 2.3.6 3.6.6.6 0 1 .4 1 1V20c0 .6-.4 1-1 1A17 17 0 013 4c0-.6.4-1 1-1h3.5c.6 0 1 .4 1 1 0 1.3.2 2.5.6 3.6.1.3 0 .7-.2 1z" fill="none" stroke="#233e85" stroke-width="1.6"/></svg></span>555-014-2280</div>
<div class="abs topbar-contact" style="left:740px">
  <span class="icon-circle"><svg width="20" height="20" viewBox="0 0 24 24"><rect x="3" y="6" width="18" height="12" rx="1.5" fill="none" stroke="#233e85" stroke-width="1.6"/><path d="M3 7l9 6 9-6" fill="none" stroke="#233e85" stroke-width="1.6"/></svg></span>sales@halvikfreight.com</div>

<div class="abs brand"><span class="brand-mark"></span>KT MACHINERY DEPOT</div>
<nav class="abs nav"><span>Home</span><span>About Us</span><span>Equipment Sales</span><span>Financing Options</span></nav>
<a class="abs btn btn-gold nav-apply">Apply Now</a>

<div class="abs badge" role="img" aria-label="Licensed used auto dealer seal"></div>
<h1 class="abs hero-title">Your Trusted Source for<br>Heavy Equipment<br>Nationwide</h1>
<p class="abs hero-text">We offer a wide range of used heavy construction equipment with the convenience of nationwide shipping. Plus, flexible financing options are available to help you get the equipment you need.</p>
<a class="abs btn btn-gold hero-btn" style="left:432px">Learn More</a>
<a class="abs btn btn-navy hero-btn" style="left:607px">Apply Now</a>

<div class="abs video" role="img" aria-label="Video still of a yellow backhoe loader parked in an equipment yard"></div>
<div class="abs play"><svg width="40" height="44" viewBox="0 0 40 44"><path d="M4 2 L38 22 L4 42 Z" fill="#233e85"/></svg></div>

<section class="abs benefits"></section>
<h2 class="abs benefits-title">Discover the unbeatable advantages of buying used heavy construction equipment today!</h2>
<p class="abs benefits-text">At KT Machinery Depot, we prioritise your needs by offering a wide selection of used heavy construction equipment. Our commitment is to ensure you find the right machinery efficiently and affordably.</p>
<div class="abs feature" style="left:128px;top:1632px"><span class="feature-icon"></span><div><h3>QUALITY EQUIPMENT AT COMPETITIVE PRICES</h3><p>We offer top-notch used equipment without breaking the bank.</p></div></div>
<div class="abs feature" style="left:440px;top:1632px"><span class="feature-icon"></span><div><h3>NATIONWIDE SHIPPING FOR YOUR CONVENIENCE</h3><p>We ship our equipment across the country, ensuring timely delivery to your location.</p></div></div>
<div class="abs feature" style="left:128px;top:1760px"><span class="feature-icon"></span><div><h3>FLEXIBLE FINANCING OPTIONS AVAILABLE</h3><p>Our financing solutions are designed to fit your budget.</p></div></div>
<div class="abs feature" style="left:440px;top:1760px"><span class="feature-icon"></span><div><h3>COMPETITIVE PRICING FOR EVERY BUDGET</h3><p>Get the best value without compromising on quality.</p></div></div>

<form class="abs finder">
  <h2>Find The Right Equipment</h2>
  <div class="field" style="left:31px;top:108px;width:278px"><span class="field-ico"></span>Select Equipment</div>
  <div class="field" style="left:31px;top:161px;width:278px"><span class="field-ico"></span>Select Make</div>
  <div class="field" style="left:31px;top:214px;width:134px;color:var(--gold)"><span class="field-ico"></span>Select Weight</div>
  <div class="field" style="left:175px;top:214px;width:134px"><span class="field-ico"></span>Select Year</div>
  <div class="field" style="left:31px;top:267px;width:278px">Enter Keyword</div>
  <a class="btn btn-navy search-btn"><svg width="16" height="16" viewBox="0 0 16 16"><circle cx="6.5" cy="6.5" r="5" fill="none" stroke="#fff" stroke-width="2"/><path d="M10.5 10.5L15 15" stroke="#fff" stroke-width="2"/></svg>Search</a>
</form>

<h2 class="abs section-title" style="top:1980px">Discover Our Featured Selection<br>of Quality Used Heavy Equipment</h2>
<p class="abs section-sub" style="top:2059px">Explore our carefully curated range of used heavy construction<br>equipment. We ensure quality and reliability in every purchase.</p>

<article class="abs card navy" style="left:142px;top:2145px"><div class="card-photo" role="img" aria-label="Compact excavator photo" style="background:linear-gradient(#c8ccd0,#8b8e8c)"></div><h3>2014 Kovara<br>KD-240 Dozer</h3><div class="price">$92,779</div><a class="btn details">View Details</a></article>
<article class="abs card gold" style="left:465px;top:2145px"><div class="card-photo" role="img" aria-label="Skid steer loader photo" style="background:linear-gradient(#b9bcbd,#77746e)"></div><span class="sold">SOLD</span><h3>2015 Baxton BX-55<br>skid steer</h3><div class="price">$92,779</div><a class="btn details">View Details</a></article>
<article class="abs card navy" style="left:788px;top:2145px"><div class="card-photo" role="img" aria-label="Orange telehandler photo" style="background:linear-gradient(#6f9ad0,#c06a3a 60%,#8a8a86)"></div><h3>2014 Stratlift<br>ST-90 Telehandler</h3><div class="price">$92,779</div><a class="btn details">View Details</a></article>
<article class="abs card gold" style="left:142px;top:2623px"><div class="card-photo" role="img" aria-label="Yellow backhoe loader photo" style="background:linear-gradient(#a7c3e0,#c9a23e 60%,#8b877f)"></div><h3>2016 Caldor CB-42<br>Backhoe</h3><div class="price">$92,779</div><a class="btn details">View Details</a></article>
<article class="abs card navy" style="left:465px;top:2623px"><div class="card-photo" role="img" aria-label="Red telehandler photo" style="background:linear-gradient(#4d7fc4,#8a4a4a 60%,#7d7b77)"></div><h3>2013 Skyreach<br>SR-108 Telehandler</h3><div class="price">$92,779</div><a class="btn details">View Details</a></article>
<article class="abs card gold" style="left:788px;top:2623px"><div class="card-photo" role="img" aria-label="Yellow dozer photo" style="background:linear-gradient(#d4d6d8,#c3a24c 60%,#8f8a80)"></div><h3>2014 Kovara<br>KD-240 Dozer</h3><div class="price">$92,779</div><a class="btn details">View Details</a></article>

<a class="abs btn btn-gold view-all">View All</a>

<h2 class="abs section-title" style="top:3292px">Client <span style="color:var(--navy)">Testimonials</span></h2>
<p class="abs section-sub" style="top:3333px">Hear what our partners and industry experts have to say</p>

<blockquote class="abs quote" style="left:135px;top:3414px">The equipment we purchased exceeded our expectations and arrived on time.</blockquote>
<blockquote class="abs quote" style="left:454px;top:3414px">Reliable service and great prices! We will definitely come back for more.</blockquote>
<blockquote class="abs quote" style="left:773px;top:3414px">KT Machinery Depot made our equipment purchase a breeze. Highly recommended!</blockquote>
<div class="abs person" style="left:135px;top:3541px"><div class="avatar" role="img" aria-label="Client portrait"></div>Dana Reyes<br>CEO, XYZ Company</div>
<div class="abs person" style="left:454px;top:3541px"><div class="avatar" role="img" aria-label="Client portrait"></div>Dana Reyes<br>CEO, XYZ Company</div>
<div class="abs person" style="left:773px;top:3541px"><div class="avatar" role="img" aria-label="Client portrait"></div>Dana Reyes<br>CEO, XYZ Company</div>

<div class="abs cta" role="img" aria-label="Dim photo of heavy equipment on a dirt job site"></div>
<h2 class="abs cta-title">Explore Our Quality Equipment Today</h2>
<p class="abs cta-text">Browse our extensive range of used heavy construction<br>equipment or contact our sales team for assistance.</p>
<a class="abs btn btn-outline cta-btn" style="left:469px">Browse</a>
<a class="abs btn btn-gold cta-btn" style="left:642px">Apply Now</a>

<div class="abs vline" style="left:359px"></div>
<div class="abs vline" style="left:748px"></div>
<nav class="abs quick"><h4>Quick Links</h4><a>Home</a><a>About Us</a><a>Equipment Sales</a><a>Financing Options</a></nav>
<div class="abs footer-brand">KT MACHINERY DEPOT<small>4820 Ridgeway Road, Dalton Creek CA 90000<br>555-014-2280</small></div>
<div class="abs socials"><span></span><span></span><span></span><span></span></div>
<address class="abs contact" style="font-style:normal">
  <h4>Contact Us</h4>
  <p><svg width="14" height="14" viewBox="0 0 24 24"><path d="M6.6 10.8a15 15 0 006.6 6.6l2.2-2.2c.3-.3.7-.4 1-.2 1.1.4 2.3.6 3.6.6.6 0 1 .4 1 1V20c0 .6-.4 1-1 1A17 17 0 013 4c0-.6.4-1 1-1h3.5c.6 0 1 .4 1 1 0 1.3.2 2.5.6 3.6.1.3 0 .7-.2 1z" fill="#a8844c"/></svg>555-014-2280</p>
  <p><svg width="14" height="14" viewBox="0 0 24 24"><rect x="2" y="5" width="20" height="14" rx="1.5" fill="#a8844c"/><path d="M2 6l10 7 10-7" fill="none" stroke="#fff" stroke-width="1.5"/></svg>sales@halvikfreight.com</p>
  <p><svg width="14" height="14" viewBox="0 0 24 24" style="flex:none"><path d="M12 2a7 7 0 00-7 7c0 5 7 13 7 13s7-8 7-13a7 7 0 00-7-7z" fill="#a8844c"/><circle cx="12" cy="9" r="2.5" fill="#fff"/></svg>Halvik Freight Inc 4820 Ridgeway Road, Dalton Creek CA 90000</p>
</address>
<div class="abs rule"></div>
<footer class="abs legal"><span>© 2024 Halvik Freight. All rights reserved.</span><a>Privacy Policy</a><a>Terms of Service</a><a>Cookies Settings</a></footer>
</body>
</html>
```